Food Safety 1-California workers only

3.25" by 4.5" Black and White Magazine Ad
This ad is to train California workers only.
Workers will be trained on: Food Safety, FSMA (Food Safety Modernization Act), using equipment safety, food processing production skills, worker safety, supervisory skills, communication skills.
"FREE TRAINING", The company does the training or Keystone Learning will provide the training.
Training grants range from $100,000 to $400,000.
Companies must be in business for profit.
Companies must train 200 employees or more.
This program is for California workers only.
Incumbent or new-hires are eligible.

Target Market(s)

California food processors, farms, food packaging, food processors, companies under FSMA, food safety, food production who need to train employees.

Industry/Entity Type

Food Production

Font styles to use
Serif
Sans Serif

Colors

Designer to choose colors to be used in the design.

Requirements
Must have
• This is a 3.25 inch by 4.5 inch magazine ad. It must be black and white. No color.
• The deliverable must be in basic PhotoShop. The ad does not need to include any graphics and be text only if needed. If you have a black and white graphic that will show well.
• Look at www.KLGFoodSafety..com
• Use the text from "MEALBOX-Photoshop-052018" file as your starting point.
Nice to have
• A black and white graphic about food. See www.KLGFoodSafety.com
Should not have
• No color.

```html
<!DOCTYPE html>
<html lang="en">
<head>
<meta charset="utf-8">
<title>Free Training – Keystone Learning</title>
<link rel="stylesheet" href="https://fonts.googleapis.com/css2?family=Open+Sans:wght@700;800&family=Source+Sans+3:wght@400;600;700&display=swap">
<style>
  :root {
    --ink: #000000;
    --paper: #ffffff;
    --text: #111111;
    --band-dark: #939393;
    --band-light: #b4b4b4;
    --backdrop: #c9ccd1;
    --photo-light: #e6e6e6;
    --photo-mid: #9d9d9d;
  }
  * { box-sizing: border-box; margin: 0; padding: 0; }
  html, body { width: 1200px; height: 1000px; overflow: hidden; }
  body {
    background: var(--backdrop);
    font-family: "Source Sans 3", "Myriad Pro", Arial, sans-serif;
    position: relative;
  }
  .ad {
    position: absolute; left: 286px; top: 65px;
    width: 628px; height: 869px;
    background: var(--paper);
    overflow: hidden;
  }
  .hero {
    position: absolute; left: 0; top: 0; width: 330px; height: 342px;
    background: var(--ink); color: var(--paper);
  }
  .headline-frame {
    position: absolute; left: 16px; top: 16px; width: 298px; height: 175px;
    border: 2px solid var(--paper);
    text-align: center;
    font-family: "Open Sans", Arial, sans-serif;
  }
  .headline-free { font-size: 92px; font-weight: 700; line-height: 1; letter-spacing: 1px; margin-top: 12px; }
  .headline-training { font-size: 47px; font-weight: 700; line-height: 1; margin-top: 8px; }
  .topics {
    position: absolute; left: 0; top: 204px; width: 100%;
    text-align: center; list-style: none;
    font-size: 23px; font-weight: 600; line-height: 32px;
  }
  .photo {
    position: absolute; left: 330px; top: 0; width: 298px; height: 342px;
    background: radial-gradient(circle at 40% 30%, var(--photo-light), var(--photo-mid) 120%);
  }
  .quote {
    position: absolute; left: 330px; top: 197px; width: 298px; height: 120px;
    background: var(--paper);
    text-align: center; font-size: 24px; line-height: 32px; color: var(--text);
    padding-top: 6px;
  }
  .quote strong { font-weight: 700; }
  .qualify-band {
    position: absolute; left: 0; top: 342px; width: 100%; height: 60px;
    background: var(--band-dark); color: var(--paper);
    text-align: center; font-size: 22px; font-weight: 700; line-height: 60px;
  }
  .criteria {
    position: absolute; left: 0; top: 413px; width: 100%;
    list-style: none; text-align: center;
    font-size: 20px; font-weight: 600; line-height: 29px; color: var(--text);
  }
  .contact-label {
    position: absolute; left: 170px; top: 641px; font-size: 21px; color: var(--text);
  }
  .contact-name {
    position: absolute; left: 267px; top: 638px; width: 361px; height: 34px;
    background: var(--ink); color: var(--paper);
    text-align: right; padding-right: 54px;
    font-size: 21px; font-weight: 700; line-height: 34px;
  }
  .company {
    position: absolute; right: 54px; top: 673px; text-align: right;
    font-size: 19px; font-weight: 700; color: var(--text); line-height: 26px;
  }
  .address {
    position: absolute; right: 54px; top: 699px; text-align: right;
    font-size: 19px; color: var(--text); line-height: 26px;
  }
  .footer {
    position: absolute; left: 0; top: 741px; width: 100%; height: 128px;
    background: var(--band-light);
    font-size: 19px; font-weight: 700; color: var(--text);
  }
  .footer-item { position: absolute; display: flex; align-items: center; }
  .footer-item svg { flex: none; }
  .web { left: 70px; top: 18px; }
  .web span { margin-left: 22px; }
  .mail { left: 68px; top: 80px; }
  .mail span { margin-left: 20px; }
  .phone { left: 400px; top: 78px; }
  .phone span { margin-left: 12px; }
</style>
</head>
<body>
  <main class="ad">
    <section class="hero">
      <div class="headline-frame">
        <div class="headline-free">FREE</div>
        <div class="headline-training">TRAINING</div>
      </div>
      <ul class="topics">
        <li>FOOD SAFETY</li>
        <li>FSMA</li>
        <li>PRODUCTION SKILLS</li>
        <li>WORKER SAFETY</li>
      </ul>
    </section>

    <div class="photo" role="img" aria-label="Black and white photo of scattered fresh fruit: cherries, raspberries and apple slices"></div>
    <p class="quote">“WE DO THE TRAINING<br>AND <strong>THE STATE<br>PAYS</strong> FOR IT!”</p>

    <div class="qualify-band">How to qualify:</div>
    <ul class="criteria">
      <li>-&nbsp; Train California Workers Only &nbsp;-</li>
      <li>- Trainees must earn $11/hour &nbsp;-</li>
      <li>-&nbsp; Full-time workers only &nbsp;-</li>
      <li>-&nbsp; Employees must attend at least 8 Hours of training &nbsp;-</li>
      <li>-&nbsp; You must train 200 or more employees &nbsp;-</li>
      <li>-&nbsp; Incumbent or New-Hire workers are eligible &nbsp;-</li>
      <li>-&nbsp; Seasonal workers are eligible &nbsp;-</li>
    </ul>

    <span class="contact-label">Contact:</span>
    <div class="contact-name">Daniel Morrow</div>
    <div class="company">Keystone Learning Company, Inc.</div>
    <div class="address">000 Harbor Crest Way, Suite 250 - Irvine, CA 92604</div>

    <footer class="footer">
      <div class="footer-item web">
        <svg width="46" height="46" viewBox="0 0 46 46" fill="none" stroke="#111" stroke-width="3">
          <circle cx="23" cy="23" r="20"/>
          <ellipse cx="23" cy="23" rx="9" ry="20"/>
          <line x1="3" y1="23" x2="43" y2="23"/>
          <path d="M7 12h32M7 34h32"/>
        </svg>
        <span>www.KLGCAL.com &nbsp;/&nbsp; www.KLGFoodSafety.com</span>
      </div>
      <div class="footer-item mail">
        <svg width="50" height="34" viewBox="0 0 50 34">
          <rect x="0" y="0" width="50" height="34" fill="#111"/>
          <path d="M2 2 L25 20 L48 2" fill="none" stroke="#b4b4b4" stroke-width="3"/>
          <path d="M2 32 L19 16 M48 32 L31 16" stroke="#b4b4b4" stroke-width="3"/>
        </svg>
        <span>Dan.Morrow@KLGCAL.com</span>
      </div>
      <div class="footer-item phone">
        <svg width="24" height="40" viewBox="0 0 24 40">
          <path d="M8 1 C3 3 0 10 1 20 C2 30 7 37 12 39 L17 38 L14 27 L9 28 C6 23 6 17 8 12 L13 11 L12 0 Z" fill="#111"/>
        </svg>
        <span>(949) 555-0148</span>
      </div>
    </footer>
  </main>
</body>
</html>
```